Expensive Jewelery and Gold Website

I require a one page template design for my site PrimeMetalReplica.example. We sell replica gold bars. Not real ones, they are novelty gifts.

I have several images of the bars (attached)
I would like a stylish and professional template layout that will be used on my site.

Designed to appear to businesses and professionals and not the members of the public.

There is no idenity or artwork for the business so you may use whichever scheme you wish to. But must somehow stylish use the images or 2-3 of the images attached.

Target Market(s)

Business and marketing professional.

Industry/Entity Type

Business

Requirements
Must have
• Incorporate some or all of images
Nice to have
• Colour/styled images to match design and look in-keeping

```html
<!DOCTYPE html>
<html lang="en">
<head>
<meta charset="utf-8">
<title>PrimeMetalReplica.example</title>
<link href="https://fonts.googleapis.com/css2?family=Roboto:wght@300;400;700;900&family=Roboto+Condensed:wght@300&family=Kaushan+Script&display=swap" rel="stylesheet">
<style>
  :root {
    --bg-top: #121314;
    --bg-body: #1a1b1d;
    --nav-bg: #1c1d1f;
    --nav-line: #2c2d30;
    --orange: #ff6a00;
    --orange-light: #ff8a12;
    --field: #d5bba4;
    --field-border: #6a4a34;
    --strip: #111213;
    --col-left: #1c1d20;
    --col-right: #222326;
    --frame: #55585c;
    --text-light: #ffffff;
    --text-muted: #6e7074;
    --nav-text: #a9abae;
  }
  * { box-sizing: border-box; margin: 0; padding: 0; }
  html, body { width: 1200px; height: 1200px; overflow: hidden; }
  body {
    position: relative;
    background: var(--bg-body);
    font-family: "Roboto", Arial, sans-serif;
    color: var(--text-light);
  }
  .masthead {
    position: absolute; left: 0; top: 0; width: 1200px; height: 253px;
    background: var(--bg-top);
  }
  .brand {
    position: absolute; left: 72px; top: 52px;
    font-family: "Roboto", Arial, sans-serif; font-weight: 300;
    font-size: 46px; letter-spacing: -1px; color: var(--text-light);
  }
  .search {
    position: absolute; left: 864px; top: 95px; width: 274px; height: 33px;
    display: flex;
  }
  .search-field {
    flex: 1; background: #1e1f21; color: #e6e6e6;
    font-size: 12px; padding: 11px 0 0 12px; letter-spacing: .3px;
  }
  .search-button { width: 33px; background: #5a5d61; }
  .main-nav {
    position: absolute; left: 68px; top: 169px; width: 1070px; height: 62px;
    background: var(--nav-bg); display: flex;
    border-top: 1px solid #26272a;
  }
  .nav-item {
    width: 153px; border-right: 1px solid var(--nav-line);
    font-size: 10.5px; letter-spacing: .8px; color: var(--nav-text);
    text-align: center; padding-top: 28px;
  }
  .nav-item:last-child { border-right: 0; }
  .nav-item.active {
    background: linear-gradient(var(--orange), var(--orange-light));
    color: #fff; height: 76px; padding-top: 38px; position: relative; z-index: 2;
  }
  .hero { position: absolute; left: 68px; top: 231px; width: 1070px; height: 440px; }
  .hero svg { position: absolute; left: 0; top: 0; }
  .hero-caption {
    position: absolute; left: 32px; top: 392px;
    font-family: "Kaushan Script", cursive; font-size: 26px; color: #fff;
  }
  .enquiry-form { position: absolute; left: 793px; top: 30px; width: 238px; }
  .enquiry-title {
    font-family: "Roboto Condensed", sans-serif; font-weight: 300;
    font-size: 42px; color: #fff; text-align: right; margin-right: -5px;
    margin-bottom: 14px; letter-spacing: -.5px;
  }
  .field-label {
    font-size: 13px; color: #fff; text-align: right; padding-right: 10px;
    letter-spacing: .5px; height: 15px; line-height: 15px;
  }
  .field {
    height: 24px; background: var(--field); border: 1px solid var(--field-border);
    border-radius: 4px; margin-bottom: 9px;
  }
  .field.message { height: 107px; margin-bottom: 15px; }
  .submit {
    margin-left: 171px; width: 64px; height: 28px; border-radius: 6px;
    background: linear-gradient(#d9dadb, #a9abad); color: #222;
    font-size: 10px; letter-spacing: .8px; text-align: center; line-height: 28px;
  }
  .strip { position: absolute; left: 68px; top: 671px; width: 1070px; height: 46px; background: var(--strip); }
  .sidebar { position: absolute; left: 68px; top: 717px; width: 379px; height: 483px; background: var(--col-left); }
  .content { position: absolute; left: 447px; top: 717px; width: 691px; height: 483px; background: var(--col-right); }
  .section-title { position: absolute; font-weight: 900; color: #fff; letter-spacing: .3px; }
  .sidebar .section-title {
    left: 30px; top: 38px; font-size: 23px; width: 320px;
    border-bottom: 1px solid #4b4d51; padding-bottom: 5px;
  }
  .content .section-title { left: 34px; top: 34px; font-size: 29px; }
  .photo-frame {
    position: absolute; width: 213px; height: 183px; background: var(--frame); padding: 10px 10px 10px 11px;
  }
  .photo-fill { width: 100%; height: 100%; }
  .fill-a { background: linear-gradient(135deg, #f4f2f0 0%, #8a4a26 45%, #5a2c14 70%, #f3f1ef 100%); }
  .fill-b { background: linear-gradient(135deg, #a7582a 0%, #2a2a2c 35%, #9b8a52 55%, #1f1f21 70%, #b4622e 100%); }
  .lead {
    position: absolute; left: 269px; top: 110px; width: 380px;
    font-size: 15px; line-height: 19.6px; color: #fff;
  }
  .body-copy {
    position: absolute; font-size: 13.3px; line-height: 19.6px; color: var(--text-muted);
  }
</style>
</head>
<body>
  <header class="masthead">
    <div class="brand">PrimeMetalReplica.example</div>
    <div class="search">
      <div class="search-field">SEARCH</div>
      <div class="search-button">
        <svg width="33" height="33" viewBox="0 0 33 33"><path d="M13 11 L21 16.5 L13 22 Z" fill="#fff"/></svg>
      </div>
    </div>
  </header>

  <nav class="main-nav">
    <div class="nav-item">HOME PAGE</div>
    <div class="nav-item active">SERVICES</div>
    <div class="nav-item">PRODUCTS</div>
    <div class="nav-item">SHOP</div>
    <div class="nav-item">TESTIMONIALS</div>
    <div class="nav-item">CONTACT US</div>
    <div class="nav-item">ENQUIRY FORM</div>
  </nav>

  <section class="hero">
    <svg width="1070" height="440" viewBox="0 0 1070 440">
      <defs>
        <linearGradient id="heroPhoto" x1="0" y1="0" x2="1" y2="1">
          <stop offset="0" stop-color="#ffffff"/>
          <stop offset=".35" stop-color="#cfcac6"/>
          <stop offset=".6" stop-color="#9d9793"/>
          <stop offset="1" stop-color="#f6f5f4"/>
        </linearGradient>
        <linearGradient id="orangeFill" x1="0" y1="0" x2="1" y2="1">
          <stop offset="0" stop-color="#ff5f00"/>
          <stop offset="1" stop-color="#ff8a10"/>
        </linearGradient>
      </defs>
      <rect width="1070" height="440" fill="#ffffff"/>
      <rect x="40" y="10" width="660" height="390" fill="url(#heroPhoto)" role="img" aria-label="Gift box wrapped in white paper with a sheer ribbon bow"/>
      <polygon points="0,393 685,393 760,440 0,440" fill="#5f6062" opacity=".95"/>
      <circle cx="1060" cy="215" r="416" fill="#ffffff"/>
      <circle cx="1060" cy="212" r="410" fill="url(#orangeFill)"/>
      <rect x="1070" y="0" width="10" height="440" fill="#ffffff"/>
    </svg>
    <div class="hero-caption">Lorum Ipsum Dolor &amp; Lorum Ipsum Dolor</div>
    <div class="enquiry-form">
      <div class="enquiry-title">enquiry today</div>
      <div class="field-label">name:</div>
      <div class="field"></div>
      <div class="field-label">telephone:</div>
      <div class="field"></div>
      <div class="field-label">email:</div>
      <div class="field"></div>
      <div class="field-label">enquiry:</div>
      <div class="field message"></div>
      <div class="submit">SUBMIT</div>
    </div>
  </section>

  <div class="strip"></div>

  <aside class="sidebar">
    <h2 class="section-title">OUR PRODUCTS</h2>
    <div class="photo-frame" style="left:35px; top:103px;">
      <div class="photo-fill fill-a" role="img" aria-label="Stacked wooden presentation boxes with a replica gold bar"></div>
    </div>
    <div class="photo-frame" style="left:35px; top:327px;">
      <div class="photo-fill fill-b" role="img" aria-label="Replica gold bar in an open wooden case on black velvet"></div>
    </div>
  </aside>

  <main class="content">
    <h1 class="section-title">INTERNAL PAGE</h1>
    <div class="photo-frame" style="left:33px; top:103px;">
      <div class="photo-fill fill-b" role="img" aria-label="Replica gold bar in an open wooden case on black velvet"></div>
    </div>
    <p class="lead">Lorem ipsum dolor sit amet, consectetur adipiscing elit. Vestibulum faucibus adipiscing turpis nec.</p>
    <p class="body-copy" style="left:269px; top:173px; width:385px;">Lorem ipsum dolor sit amet, consectetur adipiscing elit. Vestibulum faucibus adipiscing turpis nec.Lorem ipsum dolor sit amet, consectetur adipiscing elit. Vestibulum faucibus adipiscing turpis nec.Lorem ipsum dolor sit amet, consectetur adipiscing elit. Vestibulum faucibus adipiscing turpis nec.</p>
    <p class="body-copy" style="left:34px; top:326px; width:610px;">Lorem ipsum dolor sit amet, consectetur adipiscing elit. Vestibulum faucibus adipiscing turpis nec.Lorem ipsum dolor sit amet, consectetur adipiscing elit. Vestibulum faucibus adipiscing turpis nec.Lorem ipsum dolor sit amet, consectetur adipiscing elit. Vestibulum faucibus adipiscing turpis nec.</p>
    <p class="body-copy" style="left:34px; top:424px; width:610px;">Lorem ipsum dolor sit amet, consectetur adipiscing elit. Vestibulum faucibus adipiscing turpis nec.Lorem ipsum dolor sit amet, consectetur adipiscing elit. Vestibulum faucibus adipiscing turpis nec.Lorem ipsum dolor sit amet, consectetur adipiscing elit.</p>
  </main>
</body>
</html>
```